Homemaking training schools needs a Business Card design

Designer, Hello!

No special requirements, good-looking enough.
--------------------------------------------------------------------------

Name: Marcus Dale
Chairman
Tel: 0574-31759426
Mobile: 13817450926
Email: brimwell@mailtor.com
Web: www.kvd2018.com
Add: No.382, QinglanJie, BaolinQu, Ningbo, Zhejiang

LOGO
Ningbo KVD Homemaking Training School

Target Market(s)

pregnant women, mothers, infants, the elderly and families, including cleaning, cooking, nursing training.

Industry/Entity Type

Business

Contact Information for Business Card

Name: Marcus Dale
Chairman
Tel: 0574-31759426
Mobile: 13817450926
Email: brimwell@mailtor.com
Web: www.kvd2018.com

LOGO

Font styles to use
Serif
Sans Serif
Decorative

Requirements
Nice to have
• Feels: clean, specifications, safety, comfort, warmth and happiness.

```html
<!DOCTYPE html>
<html lang="en">
<head>
<meta charset="utf-8">
<title>KVD Homemaking Training School – Business Card</title>
<link rel="stylesheet" href="https://fonts.googleapis.com/css2?family=Lato:wght@400;700;900&family=Open+Sans:wght@400;600&family=Libre+Baskerville:wght@700&display=swap">
<style>
  :root {
    --backdrop: #5a5a5a;
    --card: #1d1d1f;
    --card-light: #26262a;
    --cyan: #27b6e0;
    --magenta: #e0168c;
    --brand-blue: #1f7fd8;
    --white: #ffffff;
    --soft-white: #e6e6e6;
  }
  * { margin: 0; padding: 0; box-sizing: border-box; }
  html, body { width: 1200px; height: 900px; overflow: hidden; }
  body {
    background: var(--backdrop);
    position: relative;
    font-family: "Open Sans", sans-serif;
  }
  .card {
    position: absolute;
    left: 310px;
    width: 580px;
    height: 330px;
    border-radius: 6px;
    overflow: hidden;
    background: linear-gradient(135deg, var(--card-light), var(--card));
    box-shadow: 0 14px 30px rgba(0,0,0,0.45);
  }
  .card--front { top: 70px; }
  .card--back { top: 490px; }

  .edge-band {
    position: absolute; left: 0; top: 0; bottom: 0;
    width: 26px; background: var(--cyan);
  }
  .icon-tab {
    position: absolute; left: 26px; top: 150px;
    width: 52px; height: 180px;
    background: var(--magenta);
    border-radius: 0 26px 0 0;
    display: flex; flex-direction: column; align-items: center;
    justify-content: flex-start; gap: 26px; padding-top: 18px;
  }
  .icon-tab svg { width: 22px; height: 22px; fill: var(--white); }
  .corner-tab {
    position: absolute; right: 0; bottom: 0;
    width: 120px; height: 60px;
    background: var(--cyan);
    border-radius: 26px 0 0 0;
  }

  .brand {
    position: absolute; display: flex; align-items: center; gap: 10px;
  }
  .brand__name {
    font-family: "Lato", sans-serif; font-weight: 900;
    color: var(--brand-blue); letter-spacing: 1px;
  }
  .brand__dot { border-radius: 50%; background: var(--magenta); }
  .school {
    position: absolute;
    font-family: "Libre Baskerville", serif; font-weight: 700;
    color: var(--soft-white); text-align: center; line-height: 1.45;
  }

  .card--front .brand { right: 40px; top: 34px; }
  .card--front .brand__name { font-size: 40px; }
  .card--front .brand__dot { width: 14px; height: 14px; }
  .card--front .school { right: 30px; top: 96px; width: 300px; font-size: 13px; }

  .person { position: absolute; left: 104px; top: 70px; }
  .person__name {
    font-family: "Lato", sans-serif; font-weight: 900;
    font-size: 26px; color: var(--white); text-transform: uppercase;
  }
  .person__title {
    font-family: "Lato", sans-serif; font-weight: 400;
    font-size: 14px; letter-spacing: 4px; color: var(--magenta);
    text-transform: uppercase; margin-top: 2px;
  }

  .contact { position: absolute; left: 100px; top: 164px; color: var(--soft-white); font-size: 14px; line-height: 1.35; }
  .contact__group { height: 48px; }
  .contact__group--address { color: #bdbdbd; }

  .card--back .brand { left: 50%; top: 96px; transform: translateX(-50%); }
  .card--back .brand__name { font-size: 56px; }
  .card--back .brand__dot { width: 18px; height: 18px; }
  .card--back .school { left: 0; right: 0; top: 180px; font-size: 16px; }
  .web-tab {
    position: absolute; left: 0; bottom: 0;
    width: 300px; height: 52px;
    background: var(--cyan);
    border-radius: 0 30px 0 0;
    display: flex; align-items: center; padding-left: 30px;
    font-family: "Lato", sans-serif; font-weight: 700;
    font-size: 20px; letter-spacing: 1px; color: var(--white);
  }
</style>
</head>
<body>
  <section class="card card--front">
    <div class="edge-band"></div>
    <div class="icon-tab">
      <svg viewBox="0 0 24 24" aria-hidden="true"><path d="M6.6 10.8a15.1 15.1 0 0 0 6.6 6.6l2.2-2.2c.3-.3.7-.4 1-.2 1.1.4 2.3.6 3.6.6.6 0 1 .4 1 1V20c0 .6-.4 1-1 1A17 17 0 0 1 3 4c0-.6.4-1 1-1h3.5c.6 0 1 .4 1 1 0 1.3.2 2.5.6 3.6.1.3 0 .7-.2 1z"/></svg>
      <svg viewBox="0 0 24 24" aria-hidden="true"><path d="M12 2a10 10 0 1 0 0 20 10 10 0 0 0 0-20zm6.9 6h-3a15.6 15.6 0 0 0-1.3-3.9A8 8 0 0 1 18.9 8zM12 4c.8 1.2 1.5 2.5 1.9 4h-3.8c.4-1.4 1.1-2.8 1.9-4zM4.3 14a8 8 0 0 1 0-4h3.4a16 16 0 0 0 0 4zm.8 2h3c.3 1.4.8 2.7 1.3 3.9A8 8 0 0 1 5.1 16zm3-8h-3a8 8 0 0 1 4.3-3.9C8.9 5.3 8.4 6.6 8.1 8zM12 20c-.8-1.2-1.5-2.5-1.9-4h3.8c-.4 1.4-1.1 2.8-1.9 4zm2.3-6H9.7a14.7 14.7 0 0 1 0-4h4.6a14.7 14.7 0 0 1 0 4zm.3 5.9c.5-1.2 1-2.5 1.3-3.9h3a8 8 0 0 1-4.3 3.9zm1.7-5.9a16 16 0 0 0 0-4h3.4a8 8 0 0 1 0 4z"/></svg>
      <svg viewBox="0 0 24 24" aria-hidden="true"><path d="M12 3 2 12h3v8h5v-6h4v6h5v-8h3z"/></svg>
    </div>
    <div class="corner-tab"></div>

    <div class="brand">
      <span class="brand__name">KVD</span>
      <span class="brand__dot"></span>
    </div>
    <p class="school">Ningbo KVD<br>Homemaking Training School</p>

    <div class="person">
      <h1 class="person__name">Marcus Dale</h1>
      <p class="person__title">Chairman</p>
    </div>

    <div class="contact">
      <div class="contact__group">0574-31759426<br>13817450926</div>
      <div class="contact__group">brimwell@mailtor.com<br>www.kvd2018.com</div>
      <div class="contact__group contact__group--address">No.382, QinglanJie,<br>BaolinQu, Ningbo,<br>Zhejiang</div>
    </div>
  </section>

  <section class="card card--back">
    <div class="brand">
      <span class="brand__name">KVD</span>
      <span class="brand__dot"></span>
    </div>
    <p class="school">Ningbo KVD<br>Homemaking Training School</p>
    <div class="web-tab">www.kvd2018.com</div>
  </section>
</body>
</html>
```